Web page for Gareth Pemblewick Chartered Tax Adviser

I need to take the basic web page that I have created and "Brand it" to be compatible with the corporate logo and stationery created for me by other Studio Flock designers.
I will need a watermark as well as a distinctive home page and then a branded general page for content including a series of Blogs.

Target Market(s)

My practice deals with expatriates including those looking to invest in Australia.

Industry/Entity Type

Crowd

Font styles to use
Other font styles liked:
• Per logo

Requirements
Must have
• Besides the homepage I will need a general page for content, branded in the same style as the letterheads.
Nice to have
• A watermark to go with the blogs and news content.

```html
<!DOCTYPE html>
<html lang="en">
<head>
<meta charset="utf-8">
<title>Gareth Pemblewick – Chartered Tax Adviser</title>
<link rel="stylesheet" href="https://fonts.googleapis.com/css2?family=Aleo:wght@400;700&family=Montserrat:wght@300;400&family=Arimo:wght@400&display=swap">
<style>
:root{
  --navy:#131c4e;
  --navy-deep:#0f2154;
  --steel:#1d4a72;
  --grey-band:#efefef;
  --grey-icon:#e2e2e2;
  --text:#222;
  --muted:#777;
  --white:#fff;
}
*{margin:0;padding:0;box-sizing:border-box}
html,body{width:940px;height:1200px;overflow:hidden;background:var(--white)}
body{position:relative;font-family:"Arimo",Arial,sans-serif;color:var(--text)}
.abs{position:absolute}

/* hero */
.hero-photo{left:0;top:0;width:940px;height:540px;
  background:linear-gradient(90deg,#f3f4f5 0%,#e6ebef 35%,#cdd8e0 60%,#b9c7d2 80%,#d9dfe3 100%)}
.hero-shapes{left:0;top:0}
.brand{left:134px;top:18px;display:flex;align-items:center;gap:10px}
.brand-mark{width:40px;height:40px;background:var(--navy-deep)}
.brand-text{font-family:"Aleo",Georgia,serif;font-weight:400;color:var(--navy-deep);line-height:1.1}
.brand-name{font-size:21px;letter-spacing:.5px;display:block}
.brand-sub{font-size:10px;letter-spacing:2.6px;display:block;text-transform:uppercase}
.nav{left:464px;top:31px;display:flex;gap:0;font-family:"Aleo",Georgia,serif;font-size:10px;color:var(--text)}
.nav a{color:inherit;text-decoration:none;margin-right:28px;padding-bottom:11px}
.nav a.current{border-bottom:1px solid var(--navy)}
.social{display:flex;gap:6px}
.social span{width:30px;height:33px;background:var(--grey-icon);
  clip-path:polygon(50% 0,100% 25%,100% 75%,50% 100%,0 75%,0 25%)}
.social-top{left:191px;top:76px}
.hero-kicker{left:139px;top:236px;font-family:"Aleo",Georgia,serif;font-size:17px;color:var(--navy);letter-spacing:.3px}
.hero-title{left:135px;top:250px;font-family:"Aleo",Georgia,serif;font-weight:700;font-size:62px;color:var(--navy);letter-spacing:-1px}
.btn{display:inline-block;background:var(--navy);color:var(--white);font-family:"Aleo",Georgia,serif;font-size:9px;text-align:center;text-decoration:none}
.hero-btn{left:217px;top:328px;width:153px;height:46px;line-height:46px;font-size:10px}
.dots{left:272px;top:400px;display:flex;gap:4px}
.dots span{width:12px;height:13px;background:#999;clip-path:polygon(50% 0,100% 25%,100% 75%,50% 100%,0 75%,0 25%)}
.dots span.on{background:var(--navy)}

/* services */
.service{top:555px;width:230px;text-align:center}
.service-head{display:flex;align-items:center;gap:8px;text-align:left;margin-bottom:16px}
.service-icon{width:38px;height:42px;background:var(--navy-deep);clip-path:polygon(50% 0,100% 25%,100% 75%,50% 100%,0 75%,0 25%)}
.service-title{font-family:"Montserrat",Arial,sans-serif;font-weight:300;font-size:18px;line-height:1.2;color:#111;letter-spacing:.5px}
.service-title b{font-weight:300;color:var(--steel);display:block}
.service p{font-size:9px;line-height:12.5px;color:var(--muted);margin-bottom:16px}
.service .btn{width:93px;height:30px;line-height:30px;font-size:8px}

/* reviews */
.reviews{left:0;top:753px;width:940px;height:255px;background:var(--grey-band)}
.reviews-title{left:150px;top:786px;font-family:"Aleo",Georgia,serif;font-size:33px;color:var(--steel)}
.reviews-sub{left:151px;top:825px;font-family:"Arimo",Arial,sans-serif;font-size:11px;color:#111}
.ring-dots{left:737px;top:800px;display:flex;gap:2px}
.ring-dots span{width:9px;height:9px;border:1.5px solid #555;border-radius:50%}
.client-name{left:155px;top:955px;width:82px;text-align:center;font-family:"Aleo",Georgia,serif;font-weight:700;font-size:10px;color:var(--steel)}
.quote-mark{font-family:"Aleo",Georgia,serif;font-weight:700;font-size:48px;color:var(--steel);line-height:1}
.quote-open{left:263px;top:858px}
.quote-close{left:758px;top:908px}
.quote-text{left:290px;top:883px;width:465px;font-size:10px;line-height:13px;color:#333}

/* contact */
.contact-item{top:1038px;display:flex;align-items:center;gap:14px}
.contact-item h3{font-family:"Aleo",Georgia,serif;font-weight:400;font-size:16px;color:#111}
.contact-item p{font-family:"Aleo",Georgia,serif;font-size:10px;color:var(--muted);letter-spacing:.3px;margin-top:2px}
.contact-mark{width:40px;height:40px;background:var(--steel)}
.divider{top:1030px;width:1px;height:55px;background:#e3e3e3}
.social-foot{left:689px;top:1098px}
.footer-note{left:134px;top:1150px;display:flex;align-items:center;gap:10px;font-family:"Aleo",Georgia,serif;font-size:8px;color:#dfe3ec}
.footer-note .sq{width:26px;height:26px;background:#e6e9f0}
.footer-note a{color:#5a8fd8;text-decoration:none}
</style>
</head>
<body>

<div class="abs hero-photo" role="img" aria-label="Photograph of a smiling adviser in shirt and tie seated at a bright office window"></div>
<svg class="abs hero-shapes" width="940" height="560" viewBox="0 0 940 560" aria-hidden="true">
  <defs>
    <linearGradient id="topFade" x1="0" y1="0" x2="1" y2="0">
      <stop offset="0" stop-color="#ffffff"/>
      <stop offset=".6" stop-color="#f2f2f2"/>
      <stop offset="1" stop-color="#d8d8d8"/>
    </linearGradient>
  </defs>
  <path d="M0,0 H940 V58 C820,60 680,66 600,76 C420,132 220,160 0,140 Z" fill="url(#topFade)"/>
  <path d="M14,140 C220,158 420,128 604,74 C420,138 220,166 14,140 Z" fill="#131c4e"/>
  <path d="M0,522 C240,526 520,486 940,432 V560 H0 Z" fill="#ffffff"/>
  <path d="M330,502 C520,470 720,440 940,430 C720,446 520,476 330,502 Z" fill="#131c4e"/>
</svg>

<header>
  <div class="abs brand">
    <span class="brand-mark"></span>
    <span class="brand-text"><span class="brand-name">Gareth Pemblewick</span><span class="brand-sub">Chartered Tax Adviser</span></span>
  </div>
  <nav class="abs nav">
    <a class="current" href="#">HOME</a><a href="#">ABOUT</a><a href="#">CAREER</a><a href="#">BLOG</a><a href="#">NEWS</a><a href="#">CONTACT</a>
  </nav>
  <div class="abs social social-top" aria-label="Social links"><span></span><span></span><span></span><span></span></div>
</header>

<section>
  <p class="abs hero-kicker">WE WILL SHOW YOU THE WAY TO</p>
  <h1 class="abs hero-title">SUCCESS !</h1>
  <a class="abs btn hero-btn" href="#">REACH US NOW</a>
  <div class="abs dots"><span class="on"></span><span></span><span></span></div>
</section>

<section>
  <div class="abs service" style="left:116px">
    <div class="service-head" style="margin-left:25px"><span class="service-icon" role="img" aria-label="Investment icon"></span><h2 class="service-title"><b>INVESTMENT</b>MANAGEMENT</h2></div>
    <p>Lorem ipsum dolor sit amet, consectetuerasy adipiscing elit, sed diam nonummy nibh euism tincidunt uter as laoreet dolore magna aliquam</p>
    <a class="btn" href="#">READ MORE</a>
  </div>
  <div class="abs service" style="left:356px">
    <div class="service-head" style="margin-left:25px"><span class="service-icon" role="img" aria-label="Wealth icon"></span><h2 class="service-title"><b>WEALTH</b>MANAGEMENT</h2></div>
    <p>Lorem ipsum dolor sit amet, consectetuerasy ag elit, sed diam nonummy nibh euism tincidunt uter as laoreet dolore magna aliquam</p>
    <a class="btn" href="#">READ MORE</a>
  </div>
  <div class="abs service" style="left:596px">
    <div class="service-head" style="margin-left:26px"><span class="service-icon" role="img" aria-label="Tax advisory icon"></span><h2 class="service-title"><b>TAX</b>ADVISORY</h2></div>
    <p>Sit amet, consectetuerasy adipiscing elit, sed diam nonummy nibh euism tincidunt uter as laoreet dolore magna aliquam</p>
    <a class="btn" href="#">READ MORE</a>
  </div>
</section>

<section>
  <div class="abs reviews"></div>
  <h2 class="abs reviews-title">HAPPY CLIENTS REVIEWS</h2>
  <p class="abs reviews-sub">LOREM IPSUM DOLOR SIT AMET, CONSECTETUER ELIT</p>
  <div class="abs ring-dots"><span></span><span></span><span></span></div>
  <svg class="abs" style="left:153px;top:854px" width="86" height="96" viewBox="0 0 86 96">
    <polygon points="43,2 84,25 84,71 43,94 2,71 2,25" fill="#ffffff" stroke="#1d4a72" stroke-width="3"/>
    <polygon points="43,9 78,29 78,67 43,87 8,67 8,29" fill="#b08a74" role="img" aria-label="Portrait photo of the reviewing client"/>
  </svg>
  <p class="abs client-name">MISS. CLARA</p>
  <span class="abs quote-mark quote-open">“</span>
  <p class="abs quote-text">Lorem ipsum dolor sit amet, consectetuer adipiscing elit, sed diam nonummy nibh euismod tincidunt uter as laoreet dolore magna aliquam erat volutpat. Ut wisi enim ad minim veniam, quis nostrud exerci tation they a ullamcorper suscipit lobortis nisl ut aliquip ex ea commodo consequat. Duis autem vel eum iriure dolor in as</p>
  <span class="abs quote-mark quote-close">”</span>
</section>

<footer>
  <div class="abs contact-item" style="left:133px">
    <span class="contact-mark"></span>
    <div><h3>GARETH PEMBLEWICK</h3><p>14 LARCHMERE ROW, DUNSBY UK</p></div>
  </div>
  <div class="abs divider" style="left:382px"></div>
  <div class="abs contact-item" style="left:413px">
    <svg width="42" height="42" viewBox="0 0 24 24" aria-hidden="true"><path d="M6.6 10.8a15.1 15.1 0 0 0 6.6 6.6l2.2-2.2a1 1 0 0 1 1-.25 11.4 11.4 0 0 0 3.6.57 1 1 0 0 1 1 1V20a1 1 0 0 1-1 1A17 17 0 0 1 3 4a1 1 0 0 1 1-1h3.5a1 1 0 0 1 1 1c0 1.25.2 2.45.57 3.6a1 1 0 0 1-.25 1z" fill="#1d4a72"/><path d="M15 3a6 6 0 0 1 6 6M15 6.5A2.5 2.5 0 0 1 17.5 9" stroke="#1d4a72" stroke-width="1.5" fill="none"/></svg>
    <div><h3>CALL US NOW</h3><p>020 7946 0382</p></div>
  </div>
  <div class="abs divider" style="left:608px"></div>
  <div class="abs contact-item" style="left:640px">
    <svg width="46" height="40" viewBox="0 0 46 40" aria-hidden="true"><g fill="none" stroke="#1d4a72" stroke-width="2.5"><path d="M3 14 L30 3 L40 26 L13 37 Z"/><path d="M3 14 L24 22 L30 3"/></g><path d="M30 32 H45 M34 36 H45" stroke="#1d4a72" stroke-width="2"/></svg>
    <div><h3>SEND US MAIL</h3><p>HELLO@PEMBLEWICK.EXAMPLE</p></div>
  </div>
  <div class="abs social social-foot" aria-label="Social links"><span></span><span></span><span></span><span></span></div>
  <svg class="abs" style="left:0;top:1095px" width="940" height="105" viewBox="0 0 940 105" aria-hidden="true">
    <path d="M0,34 C200,0 420,8 640,30 C760,42 860,46 940,40 V105 H0 Z" fill="#c9c9c9"/>
    <path d="M0,44 C200,14 420,20 640,40 C760,52 860,54 940,48 V105 H0 Z" fill="#ffffff"/>
    <path d="M0,56 C220,30 430,34 640,50 C770,60 870,58 940,50 V105 H0 Z" fill="#142760"/>
  </svg>
  <div class="abs footer-note"><span class="sq"></span><span>GARETH PEMBLEWICK © 2014 &nbsp;<a href="#">PRIVACY POLICY</a></span></div>
</footer>

</body>
</html>
```